Say Something About Privacy!!!

We need a poster designed with the theme of "Privacy". With so many digital assistants (Vonu, Marvo, Plinker, etc) listening to our conversations and web cams watching our activities privacy is becoming more important than ever. The goal of the project is to design a poster that can be used as giveaway item at trade shows, etc. The poster should be engaging and thought provoking. The tone can be serious or lighthearted. You can use a photo, illustration, or just copy to get your point across. I've included a few examples of other posters I like.

Target Market(s)

General Public. Well educated. Tech enthusiasts. People with smartphones and/or smart speakers.

Industry/Entity Type

Cyber Security

Font styles to use
Sans Serif

Requirements
Must have
• Simple design. Strong colours.
Should not have
• While this is a serious subject, I don't want the message to be too threatening.

```html
<!DOCTYPE html>
<html lang="en">
<head>
<meta charset="utf-8">
<title>Privacy Matters — Protect It.</title>
<link href="https://fonts.googleapis.com/css2?family=Montserrat:wght@600&family=Jost:wght@400&family=Ubuntu:wght@400&display=swap" rel="stylesheet">
<style>
  :root {
    --sun-yellow: #fcdb00;
    --signal-red: #e30000;
    --ink: #000000;
    --gold-ridge: #ebb000;
    --ghost: #fde64a;
  }
  html, body {
    margin: 0;
    padding: 0;
    width: 927px;
    height: 1200px;
    overflow: hidden;
    background: var(--sun-yellow);
  }
  .poster {
    position: relative;
    width: 927px;
    height: 1200px;
    background: var(--sun-yellow);
  }
  .poster-art {
    position: absolute;
    inset: 0;
    display: block;
  }
  .frame { fill: var(--ink); }
  .headline {
    font-family: "Montserrat", Arial, sans-serif;
    font-weight: 600;
    font-size: 170px;
    letter-spacing: -3px;
  }
  .headline-red { fill: var(--signal-red); }
  .headline-print { fill: var(--ink); }
  .subhead {
    font-family: "Jost", "Futura", sans-serif;
    font-weight: 400;
    fill: var(--signal-red);
  }
  .subhead-matters { font-size: 71px; letter-spacing: 9px; }
  .subhead-protect { font-size: 75px; letter-spacing: 15px; }
  .hashtags {
    font-family: "Ubuntu", Arial, sans-serif;
    font-size: 24px;
    fill: var(--ink);
  }
  .hashtags-ghost { fill: var(--ghost); }
</style>
</head>
<body>
  <main class="poster">
    <svg class="poster-art" width="927" height="1200" viewBox="0 0 927 1200" xmlns="http://www.w3.org/2000/svg">
      <defs>
        <radialGradient id="print-glow" cx="0.75" cy="0.62" r="0.7">
          <stop offset="0" stop-color="#ebb000" stop-opacity="0.55"/>
          <stop offset="1" stop-color="#ebb000" stop-opacity="0"/>
        </radialGradient>
      </defs>

      <g class="frame">
        <rect x="18" y="20" width="891" height="11"/>
        <rect x="18" y="20" width="11" height="1158"/>
        <rect x="18" y="1167" width="891" height="11"/>
        <rect x="898" y="20" width="11" height="588"/>
        <rect x="898" y="1123" width="11" height="55"/>
      </g>

      <g class="hashtags hashtags-ghost">
        <text x="67" y="77">#thinkprivacy</text>
        <text x="67" y="114">#privacyforeveryone</text>
      </g>

      <text class="headline" x="63" y="445"><tspan class="headline-red">PRI</tspan><tspan class="headline-print">VACY</tspan></text>

      <text class="subhead subhead-matters" x="484" y="515">MATTERS</text>

      <rect class="fingerprint-motif" x="711" y="650" width="216" height="377" fill="url(#print-glow)" role="img" aria-label="Large faint golden fingerprint decoration"/>

      <text class="subhead subhead-protect" x="64" y="1024">PROTECT IT.</text>

      <g class="hashtags">
        <text x="67" y="1093">#thinkprivacy</text>
        <text x="67" y="1130">#privacyforeveryone</text>
      </g>
    </svg>
  </main>
</body>
</html>
```